Outdoor mass notification company needing business card design.

Our company name is Harborline Signal Systems Inc located in Amory Mississippi and we sell and maintain "Corvath" Mass Notification Sirens in the US. Outdoor sirens notify people of certain severe dangers such as tornados, severe thunderstorms, flooding, hurricanes and tsunamis. We also serve the oil and gas refining industries to warn of Chemical releases, fires, and lightning alerts.

Contact Information for Business Card

Name, title, cell number, email address

Requirements
Nice to have
• The Corvath logo and also the Tallbrook logo.

```html
<!DOCTYPE html>
<html lang="en">
<head>
<meta charset="utf-8">
<title>Harborline Signal Systems – Business Card</title>
<link href="https://fonts.googleapis.com/css2?family=Cinzel:wght@700&family=Montserrat:wght@400;500&display=swap" rel="stylesheet">
<style>
  :root {
    --backdrop: #d4d4d4;
    --paper: #ffffff;
    --navy: #3b5873;
    --navy-deep: #2a4259;
    --ink: #2d4a66;
    --swoosh: #8c8c8c;
    --white: #ffffff;
    --siren-dark: #3a3a3a;
    --siren-light: #8a8a8a;
  }
  * { box-sizing: border-box; margin: 0; padding: 0; }
  html, body { width: 1200px; height: 802px; overflow: hidden; }
  body {
    background: var(--backdrop);
    display: flex;
    align-items: center;
    justify-content: center;
    gap: 50px;
    font-family: "Montserrat", sans-serif;
  }
  .card {
    position: relative;
    width: 520px;
    height: 300px;
    border-radius: 22px;
    overflow: hidden;
    box-shadow: 0 6px 18px rgba(0,0,0,0.18);
  }
  .card-front { background: var(--paper); }
  .card-back {
    background: var(--navy);
    display: flex;
    align-items: center;
    justify-content: center;
  }
  .wave { position: absolute; inset: 0; width: 100%; height: 100%; }
  .wordmark {
    font-family: "Cinzel", serif;
    font-weight: 700;
    color: var(--ink);
    text-align: center;
    line-height: 1.05;
  }
  .card-front .wordmark {
    position: absolute;
    top: 26px;
    left: 150px;
    font-size: 24px;
  }
  .wordmark .line-small { display: block; font-size: 0.72em; letter-spacing: 0.02em; }
  .card-back .wordmark { font-size: 44px; color: var(--navy-deep); }
  .siren-photo {
    position: absolute;
    top: 22px;
    left: 420px;
    width: 60px;
    height: 130px;
    border-radius: 6px;
    background: linear-gradient(180deg, var(--siren-dark) 0%, var(--siren-light) 55%, var(--siren-dark) 100%);
  }
  .contact {
    position: absolute;
    left: 34px;
    bottom: 22px;
    color: var(--white);
  }
  .contact-name {
    font-family: "Cinzel", serif;
    font-weight: 700;
    font-size: 19px;
    letter-spacing: 0.03em;
    line-height: 1.2;
  }
  .contact-title { font-size: 12px; margin-bottom: 6px; }
  .rule { width: 14px; height: 1px; background: var(--white); margin-bottom: 6px; }
  .contact-list { list-style: none; font-size: 12.5px; }
  .contact-list li { display: flex; align-items: center; gap: 7px; margin-top: 3px; }
  .contact-list svg { width: 11px; height: 11px; fill: var(--white); }
</style>
</head>
<body>
  <section class="card card-front">
    <svg class="wave" viewBox="0 0 520 300" preserveAspectRatio="none" aria-hidden="true">
      <path d="M0,136 C150,126 250,106 330,76 C400,48 450,34 520,28" fill="none" stroke="var(--swoosh)" stroke-width="6"/>
      <path d="M0,300 L0,150 C150,140 250,120 330,90 C400,62 450,48 520,42 L520,300 Z" fill="var(--navy)"/>
    </svg>
    <div class="wordmark">HARBORLINE<span class="line-small">SIGNAL SYSTEMS</span></div>
    <div class="siren-photo" role="img" aria-label="Photo of an outdoor mass notification siren on a pole"></div>
    <div class="contact">
      <p class="contact-name">DORIAN VALE</p>
      <p class="contact-title">CEO/Founder</p>
      <div class="rule"></div>
      <ul class="contact-list">
        <li><svg viewBox="0 0 24 24"><path d="M6.6 10.8a15 15 0 0 0 6.6 6.6l2.2-2.2a1 1 0 0 1 1-.25 11.4 11.4 0 0 0 3.6.57 1 1 0 0 1 1 1V20a1 1 0 0 1-1 1A17 17 0 0 1 3 4a1 1 0 0 1 1-1h3.5a1 1 0 0 1 1 1c0 1.25.2 2.45.57 3.6a1 1 0 0 1-.25 1z"/></svg>(662)555-0147</li>
        <li><svg viewBox="0 0 24 24"><path d="M2 5h20v14H2z M2 5l10 8 10-8"/></svg>info@harborlinesignal.com</li>
        <li><svg viewBox="0 0 24 24"><circle cx="12" cy="12" r="10"/></svg>www.harborlinesignal.com</li>
      </ul>
    </div>
  </section>

  <section class="card card-back">
    <div class="wordmark">HARBORLINE<span class="line-small">SIGNAL SYSTEMS</span></div>
  </section>
</body>
</html>
```